Family owned plumbing contractor needs eye catching business card design

Business cards that are unique, eye catching, and provide customers with general company information, such as name, address, phone number, website, employee name/title, cell phone #, & email address. We are transitioning to a new logo that utilizes a more retro feel, so we are interested in seeing some cool old school designs in the mix. We are liking the dark background on some of the samples on this website. If that is workable with our artwork, we would like to see that incorporated into the design.
Contact Information for Business Card
Copperline Pipeworks, Inc.
www.copperlinepipeworks.example
(555) 392-7068 phone
Nevada License #64205
California License #5810473
Dale Wrennick, President
(555) 618-9032 cell
dale@copperlinepipeworks.example
Residential * Commercial * Service
Requirements
Must have
- The business card details listed above & logo provided.
Nice to have
- I made some notes about color options in the description.

```html
<!DOCTYPE html>
<html lang="en">
<head>
<meta charset="utf-8">
<title>Copperline Pipeworks Business Card</title>
<link href="https://fonts.googleapis.com/css2?family=Roboto+Condensed:wght@400;700&display=swap" rel="stylesheet">
<style>
  :root {
    --slate: #5f7f99;
    --slate-dark: #4a6680;
    --teal: #7cc8bc;
    --white: #ffffff;
    --stage: #1e1f23;
  }
  * { box-sizing: border-box; margin: 0; padding: 0; }
  html, body { width: 1200px; height: 800px; overflow: hidden; }
  body {
    background: var(--stage);
    font-family: "Roboto Condensed", Arial, sans-serif;
    color: var(--white);
    display: flex;
    align-items: center;
    justify-content: center;
    gap: 40px;
  }
  .card {
    position: relative;
    width: 540px;
    height: 309px;
    background: var(--slate);
    overflow: hidden;
  }
  .brand-mark {
    display: flex;
    align-items: center;
    gap: 10px;
    color: var(--slate-dark);
    font-weight: 700;
    font-size: 22px;
    line-height: 1.1;
  }
  .brand-mark .dot {
    width: 22px; height: 22px;
    border-radius: 50%;
    background: var(--teal);
    flex: none;
  }
  /* Front */
  .card-front .brand-mark {
    position: absolute;
    left: 50%; top: 108px;
    transform: translateX(-50%);
    color: var(--white);
    font-size: 26px;
    white-space: nowrap;
  }
  .services {
    position: absolute;
    left: 0; right: 0; bottom: 70px;
    text-align: center;
    font-size: 14px;
    letter-spacing: 2.5px;
    font-weight: 700;
  }
  .services .star { margin: 0 6px; }
  /* Back */
  .card-back .shape { position: absolute; left: 0; top: 0; }
  .card-back .brand-mark {
    position: absolute;
    left: 50px; top: 62px;
    width: 210px;
  }
  .company-name {
    position: absolute;
    right: 30px; top: 26px;
    text-align: right;
    font-weight: 700;
    font-size: 20px;
    line-height: 1.05;
    text-transform: uppercase;
  }
  .company-details {
    position: absolute;
    right: 30px; top: 150px;
    text-align: right;
    font-size: 13px;
    line-height: 1.25;
  }
  .company-details b { font-weight: 700; }
  .website {
    position: absolute;
    right: 30px; top: 222px;
    font-weight: 700;
    font-size: 13px;
  }
  .person {
    position: absolute;
    left: 70px; top: 190px;
    font-size: 13px;
    line-height: 1.2;
  }
  .person-name { font-weight: 700; font-size: 22px; line-height: 1; }
  .person-title { margin-bottom: 8px; }
  .person b { font-weight: 700; }
</style>
</head>
<body>
  <section class="card card-front">
    <div class="brand-mark"><span class="dot"></span>Copperline Pipeworks, Inc.</div>
    <p class="services"><span class="star">✱</span>Residential <span class="star">✱</span>Commercial <span class="star">✱</span>Service</p>
  </section>

  <section class="card card-back">
    <svg class="shape" width="540" height="309" viewBox="0 0 540 309" aria-hidden="true">
      <path d="M0,0 H312 C352,38 368,110 345,148 C330,168 310,174 285,174 H0 Z" fill="var(--teal)"/>
      <path d="M0,0 H292 C328,36 340,108 320,145 C306,166 290,174 265,174 H0 Z" fill="var(--white)"/>
    </svg>
    <div class="brand-mark"><span class="dot"></span>Copperline Pipeworks, Inc.</div>
    <h1 class="company-name">Copperline<br>Pipeworks, Inc.</h1>
    <p class="company-details">
      <b>Phone:</b>(555) 392-7068<br>
      Nevada License #64205<br>
      California License #5810473
    </p>
    <p class="website">www.copperlinepipeworks.example</p>
    <div class="person">
      <p class="person-name">Dale Wrennick</p>
      <p class="person-title">President</p>
      <p><b>Cell:</b> (555) 618-9032</p>
      <p>dale@copperlinepipeworks.example</p>
    </div>
  </section>
</body>
</html>
```